Flyer / Mailer for Business Debt Relief Business - Harborline Relief 6" x 11"

We need a 6" x 11" double sided flyer. This will be sent out to potential customers with high interest business loans. We would like the design to coordinate with the colors of our logo. I have included a mock up that we sketched out. I have also included a file of a mailer we received that we would like to use as a template (not colors or fonts, just set up). I have also included an .ai file of our logo.

```html
<!DOCTYPE html>
<html lang="en">
<head>
<meta charset="utf-8">
<title>Harborline Relief – Mailer</title>
<link href="https://fonts.googleapis.com/css2?family=Montserrat:ital,wght@0,300;0,400;0,500;0,600;1,700&display=swap" rel="stylesheet">
<style>
  :root{
    --bg:#e9e9ea;
    --green:#82b616;
    --blue:#1b5aa0;
    --blue-bright:#1e88d0;
    --ink:#4a4a4a;
    --grey-panel:#eceef0;
    --white:#ffffff;
  }
  *{box-sizing:border-box;margin:0;padding:0}
  html,body{width:1200px;height:1200px;overflow:hidden}
  body{background:var(--bg);font-family:'Montserrat',sans-serif;position:relative}

  .card{position:absolute;left:189px;width:822px;height:442px;background:var(--white);overflow:hidden}
  .card--front{top:112px}
  .card--back{top:638px}

  /* front: photo column */
  .photo{position:absolute;left:0;width:161px}
  .photo--coins{top:0;height:106px;background:linear-gradient(135deg,#cfd8b4,#b89a5e 70%,#8a6a38)}
  .photo--jars{top:112px;height:106px;background:linear-gradient(180deg,#f3f4f2,#c9c6bf)}
  .photo--sprouts{top:224px;height:84px;background:linear-gradient(135deg,#e8b53a,#b8861c 60%,#6f5216)}
  .photo--hands{top:314px;height:128px;background:linear-gradient(180deg,#f4f4f2,#e6d7bf)}

  .bands{position:absolute;left:0;top:0}

  .headline{position:absolute;left:190px;top:20px;color:var(--white);font-weight:600;font-size:28px;line-height:26px;letter-spacing:.2px}
  .subhead{position:absolute;left:188px;top:95px;color:var(--white);font-weight:500;font-size:17px;line-height:16px}

  .brand{position:absolute;text-align:center;color:var(--ink);font-weight:400;letter-spacing:.5px}
  .brand__mark{display:block;margin:0 auto 12px;background:var(--green)}
  .brand--front{left:640px;top:22px;width:168px;font-size:15px}
  .brand--front .brand__mark{width:50px;height:50px}

  .panel{position:absolute;left:161px;top:141px;width:661px;height:227px;background:linear-gradient(90deg,#e2e4e7,#f4f5f6)}
  .portrait{position:absolute;left:531px;top:141px;width:291px;height:227px;background:linear-gradient(180deg,#d8dadc 0%,#b9bcbf 45%,#4b4f55 100%)}

  .question{position:absolute;left:195px;top:153px;font-style:italic;font-weight:700;font-size:17.5px;color:#5a5a5a}
  .cta-big{position:absolute;left:193px;top:172px;font-weight:300;font-size:62px;letter-spacing:-3px;color:var(--blue-bright);line-height:70px}
  .benefits{position:absolute;left:190px;top:236px;list-style:none;font-size:10.5px;line-height:13.8px;color:#555}
  .benefits li::before{content:"• "}

  .contact-bar{position:absolute;left:161px;top:368px;width:661px;height:74px;background:var(--blue)}
  .contact-bar__accent{position:absolute;right:0;bottom:0}
  .phone{position:absolute;left:30px;top:10px;display:flex;align-items:center;gap:3px;color:var(--green);font-weight:600;font-size:30px}
  .divider{position:absolute;left:276px;top:14px;width:1px;height:30px;background:var(--white)}
  .web{position:absolute;left:295px;top:11px;color:var(--white);font-weight:500;font-size:14px;line-height:18px}
  .email{position:absolute;right:26px;bottom:4px;color:var(--white);font-weight:500;font-size:10.5px}

  /* back */
  .brand--back{left:39px;top:34px;width:143px;font-size:14.5px}
  .brand--back .brand__mark{width:56px;height:56px;margin-bottom:14px}
  .address{position:absolute;left:20px;top:146px;width:180px;text-align:center;font-size:9.5px;line-height:11.5px;color:#333}
  .tagline{position:absolute;left:31px;top:208px;color:var(--blue);font-weight:600;font-size:16.5px;line-height:18.5px}
  .pitch{position:absolute;left:31px;top:268px;color:#222;font-weight:500;font-size:16px;line-height:20.3px}
</style>
</head>
<body>

<section class="card card--front">
  <div class="photo photo--coins" role="img" aria-label="Hand stacking gold coins in rising piles"></div>
  <div class="photo photo--jars" role="img" aria-label="Glass jars of coins with green sprouts"></div>
  <div class="photo photo--sprouts" role="img" aria-label="Seedlings growing from coin stacks in golden light"></div>
  <div class="photo photo--hands" role="img" aria-label="Cupped hands holding coins and a young plant"></div>

  <svg class="bands" width="822" height="141" viewBox="0 0 822 141">
    <polygon points="161,0 636,0 611,77 161,77" fill="#82b616"/>
    <polygon points="636,0 660,0 611,77 605,77" fill="#6a9a10"/>
    <polygon points="161,77 610,77 688,141 161,141" fill="#1b5aa0"/>
    <polygon points="610,77 630,77 688,141 668,141" fill="#1e88d0"/>
  </svg>

  <h1 class="headline">HELPING BUSINESS FOCUS<br>ON WHAT MATTERS!</h1>
  <p class="subhead">We understand that merchant cash advance loans<br>can be a burden on your business.</p>

  <div class="brand brand--front"><span class="brand__mark"></span>HARBORLINE RELIEF</div>

  <div class="panel"></div>
  <div class="portrait" role="img" aria-label="Smiling businessman in a suit giving a thumbs up in an office"></div>

  <p class="question">Over Whelmed by daily/weekly payments?</p>
  <p class="cta-big">WE CAN HELP!</p>
  <ul class="benefits">
    <li>This is not a loan, WE ARE NOT LENDERS!</li>
    <li>Improve your business cash flow immediately.</li>
    <li>Move Payment to one monthly amount.</li>
    <li>Reduce the amount you are paying out monthly.</li>
    <li>Strategic alternatives to high interest loans.</li>
    <li>Fast, confidential business debt relief.</li>
    <li>No-obligation consultation.</li>
    <li>Absolutely no credit polls.</li>
    <li>No collateral, no financials.</li>
  </ul>

  <div class="contact-bar">
    <svg class="contact-bar__accent" width="270" height="20" viewBox="0 0 270 20">
      <polygon points="20,0 270,0 270,20 0,20" fill="#1e88d0"/>
    </svg>
    <div class="phone">
      <svg width="14" height="18" viewBox="0 0 14 18"><path d="M9 1 C3 3 2 15 9 17 L11 13 L8 11 C7 9 7 8 8 6 L11 5 Z" fill="none" stroke="#82b616" stroke-width="1.5"/></svg>
      844-555-0182
    </div>
    <div class="divider"></div>
    <p class="web">Visit our website: www.harborlinetoday.com<br>Call now for free consultation with our experts</p>
    <p class="email">E-mail: info@harborlinetoday.com</p>
  </div>
</section>

<section class="card card--back">
  <div class="brand brand--back"><span class="brand__mark"></span>HARBORLINE RELIEF</div>
  <p class="address">4820 Meadow Park Dr<br>Riverton, Hale County 75310<br>USA</p>
  <h2 class="tagline">STRATEGIC DEBT RELIEF FOR<br>BUSINESS OF ALL SIZES.</h2>
  <p class="pitch">Stop taking out loans to<br>pay off other loans.<br>Take back your business's<br>cash flow, and focus on<br>what matters.</p>
</section>

</body>
</html>
```